I need a design to display a result on a range line

For example - If I have a blood sugar result and I want to display it on a line so that I can display it in picture terms so that it can be understood more.
I want to input the result in a calculator so it can be displayed on the range line.

I want it so I can customise it and apply it to other results my self too.

```html
<!DOCTYPE html>
<html lang="en">
<head>
<meta charset="utf-8">
<title>Blood Sugar Range Line</title>
<link rel="stylesheet" href="https://fonts.googleapis.com/css2?family=Lato:wght@700;900&display=swap">
<style>
  :root {
    --bg: #ffffff;
    --ink: #000000;
    --ink-soft: #2b2b2b;
    --unit: #9a9a9a;
    --label-muted: #9b9b9b;
    --divider: #8a8a8a;
    --red: #a51f18;
    --slate: #6f7a78;
    --teal: #52bcbf;
    --mint: #79d6be;
    --sand: #e6dac4;
    --peach: #f3d3b9;
    --salmon: #e28d76;
    --marker-alert: #ff4a00;
    --marker-good: #66ff00;
  }
  * { margin: 0; padding: 0; box-sizing: border-box; }
  html, body { width: 1200px; height: 900px; overflow: hidden; background: var(--bg); }
  body { font-family: "Lato", sans-serif; position: relative; }

  .gauge { position: absolute; left: 0; top: 0; width: 1200px; height: 900px; }

  .range-bar {
    position: absolute; left: 135px; width: 916px; height: 54px; border-radius: 27px;
  }
  .gauge--labels-above .range-bar {
    top: 240px;
    background: linear-gradient(90deg, var(--red) 0%, var(--red) 6%, var(--slate) 12%, var(--teal) 30%, var(--mint) 40%, var(--sand) 51%, var(--peach) 61%, var(--salmon) 76%, var(--red) 88%, var(--red) 100%);
  }
  .gauge--labels-below .range-bar {
    top: 557px;
    background: linear-gradient(90deg, var(--red) 0%, var(--red) 5%, var(--slate) 24%, var(--teal) 38%, var(--mint) 50%, var(--sand) 61%, var(--peach) 70%, var(--salmon) 81%, var(--red) 88%, var(--red) 100%);
  }

  .divider { position: absolute; width: 1px; background: var(--divider); }
  .gauge--labels-above .divider { top: 164px; height: 76px; }
  .gauge--labels-below .divider { top: 611px; height: 11px; }

  .bound {
    position: absolute; font-size: 19px; font-weight: 900; color: var(--ink);
    line-height: 22px; white-space: nowrap;
  }
  .bound .unit { font-size: 14px; font-weight: 700; color: var(--unit); margin-left: 4px; }
  .gauge--labels-above .bound { top: 164px; }
  .gauge--labels-below .bound { top: 534px; }
  .bound--end { text-align: right; }

  .zone {
    position: absolute; font-size: 20px; font-weight: 900; line-height: 24px;
    transform: translateX(-50%); white-space: nowrap;
  }
  .gauge--labels-above .zone { top: 198px; color: var(--label-muted); }
  .gauge--labels-below .zone { top: 623px; color: var(--ink-soft); }

  .result-dot { position: absolute; width: 30px; height: 30px; border-radius: 50%; }
  .result-dot--alert { background: var(--marker-alert); left: 703px; top: 252px; }
  .result-dot--good { background: var(--marker-good); left: 426px; top: 569px; }

  .result-value {
    position: absolute; font-size: 20px; font-weight: 900; color: var(--ink);
    line-height: 24px; white-space: nowrap;
  }
  .result-value .unit { font-size: 14px; font-weight: 700; color: var(--ink-soft); margin-left: 4px; }
  .result-value--top { left: 748px; top: 256px; }
  .result-value--bottom { left: 471px; top: 572px; }
</style>
</head>
<body>

<section class="gauge gauge--labels-above" aria-label="Blood sugar result, labels above">
  <span class="bound bound--end" style="right:843px">3.99<span class="unit">mmol/L</span></span>
  <span class="bound" style="left:367px">4.0</span>
  <span class="bound bound--end" style="right:599px">5.59<span class="unit">mmol/L</span></span>
  <span class="bound" style="left:612px">5.6</span>
  <span class="bound bound--end" style="right:339px">6.99<span class="unit">mmol/L</span></span>
  <span class="bound" style="left:873px">7</span>

  <span class="zone" style="left:270px">Low</span>
  <span class="zone" style="left:466px">Optimal</span>
  <span class="zone" style="left:718px">Pre-Diabetic</span>
  <span class="zone" style="left:949px">High</span>

  <span class="divider" style="left:361px"></span>
  <span class="divider" style="left:606px"></span>
  <span class="divider" style="left:867px"></span>

  <div class="range-bar"></div>
  <span class="result-dot result-dot--alert"></span>
  <span class="result-value result-value--top">4.59<span class="unit">mmol/L</span></span>
</section>

<section class="gauge gauge--labels-below" aria-label="Blood sugar result, labels below">
  <span class="bound bound--end" style="right:842px">3.99<span class="unit">mmol/L</span></span>
  <span class="bound" style="left:368px">4.0</span>
  <span class="bound bound--end" style="right:598px">5.59<span class="unit">mmol/L</span></span>
  <span class="bound" style="left:613px">5.6</span>
  <span class="bound bound--end" style="right:338px">6.99<span class="unit">mmol/L</span></span>
  <span class="bound" style="left:874px">7</span>

  <div class="range-bar"></div>

  <span class="divider" style="left:362px"></span>
  <span class="divider" style="left:607px"></span>
  <span class="divider" style="left:868px"></span>

  <span class="zone" style="left:250px">Low</span>
  <span class="zone" style="left:470px">Optimal</span>
  <span class="zone" style="left:734px">Pre-Diabetic</span>
  <span class="zone" style="left:964px">High</span>

  <span class="result-dot result-dot--good"></span>
  <span class="result-value result-value--bottom">4.59<span class="unit">mmol/L</span></span>
</section>

</body>
</html>
```